KV Group

We need a new website for our company and since we had a very good work done for our logo in this site, we're back for the entire job.

Our company name is Marlowe Capital Group. We're adding files of examples of what we have done today. In my opinion we need a more attention lock in the site but yet financial simple work.

Our files (attached) will let you know what we have so far. We need a complete change but the colours should be the same, however you can change them not running away to far from the original, and of course matching with the logo.

We need examples for 3 kind of layouts.

- A HOME welcome layout
- An internal Layout with sidebar
- And internal Layout wide

We can buy image licenses if needed for assets.
Actually there are 5 slide images placed on the Welcome HOME, we need those there, but you can improve with better images to match the new website!!!

Target Market(s)

Clients looking for financial advisers, tax and funds specialist, currency advisers

Industry/Entity Type

Financial

Requirements
Must have
• all the fonts must be in accordance with the financial market sites........the welcome home page must be precise, neat and information accurate........the menu should be elegant........main focus on the Home page, should be also the PRIVATE ACCESS box log in.......

```html
<!DOCTYPE html>
<html lang="en">
<head>
<meta charset="utf-8">
<title>Marlowe Capital Group</title>
<link href="https://fonts.googleapis.com/css2?family=Ubuntu:wght@300;400;500&display=swap" rel="stylesheet">
<style>
:root{
  --orange:#ef7a1e;
  --orange-dark:#a84a07;
  --ink:#333;
  --muted:#777;
  --light:#999;
  --footer:#262626;
  --footer-text:#cfcfcf;
}
*{margin:0;padding:0;box-sizing:border-box}
html,body{width:746px;height:1200px;overflow:hidden;background:#fff}
body{position:relative;font-family:'Ubuntu',sans-serif;color:var(--ink)}
.abs{position:absolute}
.header{left:0;top:0;width:746px;height:105px;border-bottom:1px solid #e6e6e6}
.logo{left:52px;top:40px;display:flex;align-items:center;gap:8px}
.logo-mark{width:22px;height:22px;background:var(--orange)}
.logo-name{font-size:14px;font-weight:400;letter-spacing:1px;color:#222}
.btn-top{top:33px;height:23px;border-radius:3px;color:#fff;font-size:9.5px;display:flex;align-items:center;justify-content:center;gap:4px}
.btn-apply{left:505px;width:86px;background:var(--orange)}
.btn-contact{left:604px;width:86px;background:#3a3a3a}
.nav{left:240px;top:74px;display:flex;font-size:11.5px;color:#333}
.nav span{padding:0 8px;border-left:1px solid #bbb;line-height:12px}
.nav span:first-child{border-left:0;padding-left:0}
.nav span:last-child{padding-right:0}
.hero{left:0;top:105px;width:746px;height:292px;background:linear-gradient(90deg,#f6f9fb 0%,#eef3f8 40%,#dfe8f1 100%)}
.hero-photo{left:300px;top:0;width:446px;height:292px;background:linear-gradient(90deg,rgba(238,243,248,0) 0%,#e7d7c8 30%,#d7dde6 70%,#e9e2e6 100%)}
.hero h1{left:54px;top:72px;font-size:27px;font-weight:400;color:var(--orange)}
.hero h2{left:54px;top:105px;font-size:21.5px;font-weight:300;color:var(--orange-dark)}
.hero p{left:55px;top:137px;width:280px;font-size:9px;line-height:15px;color:#666}
.dots{left:56px;top:180px;display:flex;gap:3px}
.dots i{width:10px;height:10px;border-radius:50%;background:#d8cbbf}
.dots i:first-child{background:var(--orange-dark)}
.welcome{left:0;top:424px;width:746px;text-align:center}
.welcome h2{font-size:21px;font-weight:300;color:#333}
.welcome p{margin:5px auto 0;width:590px;font-size:8.3px;line-height:14px;color:#666}
.card{top:512px;width:186px;height:207px;border:1px solid #e2e2e2;border-radius:3px;box-shadow:0 1px 3px rgba(0,0,0,.08);text-align:center;overflow:hidden}
.card-img{height:96px}
.card h3{margin-top:10px;font-size:12.5px;font-weight:400;color:var(--orange)}
.card p{margin:4px auto 0;width:160px;font-size:7.6px;line-height:14px;color:var(--light)}
.read{display:inline-block;margin-top:6px;width:71px;height:20px;line-height:20px;background:var(--orange);color:#fff;font-size:7.5px;border-radius:2px}
.about h2{font-size:18px;font-weight:400;color:#333}
.about .lead{margin-top:6px;font-size:9.5px;line-height:14px;color:#555}
.about .body{margin-top:6px;font-size:7.8px;line-height:14px;color:#666}
.badges{left:66px;top:903px;display:flex;align-items:center}
.badge{height:30px;background:#e8e8e8;border-radius:3px}
.sep{width:1px;height:30px;background:#ddd;margin:0 28px}
.access{left:494px;top:770px;width:196px;height:169px;border-radius:3px;background:linear-gradient(180deg,#c66a10 0%,#9a4204 100%);border:1px solid #8a3c05;padding:12px 18px;color:#fff}
.access h2{font-size:17px;font-weight:300}
.access p{margin-top:3px;font-size:7px;line-height:12px;color:#f3c89e}
.field{margin-top:7px;height:19px;background:#fff;border-radius:2px;font-size:7px;color:#aaa;padding:5px 8px}
.forgot{margin-top:10px;display:flex;justify-content:space-between;align-items:center;font-size:7px;padding-left:4px}
.login{width:46px;height:18px;background:var(--orange);border-radius:2px;text-align:center;line-height:18px;font-size:8.5px}
.footer{left:0;top:967px;width:746px;height:233px;background:var(--footer);border-top:4px solid #dedede}
.col{top:27px;color:var(--footer-text)}
.col h4{font-size:12.5px;font-weight:400;color:#fff;margin-bottom:5px}
.col li{list-style:none;font-size:8px;line-height:15.8px}
.col h4.second{margin-top:12px}
.rule{left:51px;top:174px;width:644px;height:1px;background:#3f3f3f}
.copy{left:59px;top:189px;font-size:8px;color:#888}
.social{left:607px;top:189px;display:flex;gap:5px}
.social i{width:16px;height:16px;border-radius:2px}
</style>
</head>
<body>
<header class="abs header">
  <div class="abs logo"><div class="logo-mark"></div><div class="logo-name">MARLOWE CAPITAL</div></div>
  <div class="abs btn-top btn-apply">
    <svg width="10" height="10" viewBox="0 0 10 10"><circle cx="5" cy="3" r="2.2" fill="#fff"/><path d="M1 10c0-3 2-4.5 4-4.5S9 7 9 10z" fill="#fff"/></svg>APPLY NOW</div>
  <div class="abs btn-top btn-contact">
    <svg width="10" height="10" viewBox="0 0 10 10"><path d="M2 1l2 2-1 1.5c.6 1.2 1.3 1.9 2.5 2.5L7 6l2 2-1.5 1.5C4.5 9 1 5.5.5 2.5z" fill="#fff"/></svg>CONTACT US</div>
  <nav class="abs nav"><span>HOME</span><span>ABOUT US</span><span>INVESTMENTS</span><span>FUNDS</span><span>BROKERAGE</span><span>EXCHANGE</span><span>ACCOUNTS</span></nav>
</header>

<section class="abs hero">
  <div class="abs hero-photo" role="img" aria-label="Photo of a young woman holding a pink piggy bank"></div>
  <h1 class="abs">Donec scelerisque leo</h1>
  <h2 class="abs">Phasellus felis dolor scelerisque</h2>
  <p class="abs">Mivamus porttitor, g, purus nisi eleifend libero, a tempus libero lectus feugiat felis. Morbi diam mauris, viverra</p>
  <div class="abs dots"><i></i><i></i><i></i><i></i></div>
</section>

<section class="abs welcome">
  <h2>Welcome to Marlowe Capital Group</h2>
  <p>Phasellus felis dolor, scelerisque a, tempus eget, lobortis id, libero. Donec scelerisque leo ac risus. Praesent sit amet est. In dictum, dolor eu dictum porttitor, enim felis viverra mi, eget luctus massa purus quis odio. Etiam nulla massa, pharetra facilisis, volutpat in, imperdiet sit amet, sem.</p>
</section>

<article class="abs card" style="left:76px">
  <div class="card-img" role="img" aria-label="Photo of hands with a pen over a bar chart report" style="background:linear-gradient(135deg,#e9ecef,#c9d8c0 60%,#9fc9d6)"></div>
  <h3>Management &amp; Stategy</h3>
  <p>Mauris neque metus malesuada nec ultricies sit amet porttitor mattis enim. In massa libero interdum nec</p>
  <span class="read">READ MORE</span>
</article>
<article class="abs card" style="left:279px">
  <div class="card-img" role="img" aria-label="Photo of two businessmen reviewing documents" style="background:linear-gradient(135deg,#c9d6e6,#2e3e5c 55%,#dfe6ee)"></div>
  <h3>Funds</h3>
  <p>Mauris neque metus malesuada nec ultricies sit amet porttitor mattis enim. In massa libero interdum nec</p>
  <span class="read">READ MORE</span>
</article>
<article class="abs card" style="left:482px">
  <div class="card-img" role="img" aria-label="Illustration of golden currency symbols" style="background:linear-gradient(135deg,#8a5a0c,#e3a935 50%,#f5d27a)"></div>
  <h3>Currency Exchange</h3>
  <p>Mauris neque metus malesuada nec ultricies sit amet porttitor mattis enim. In massa libero interdum nec</p>
  <span class="read">READ MORE</span>
</article>

<section class="abs about" style="left:63px;top:770px;width:405px">
  <h2>Little About Our Company</h2>
  <p class="lead">Lorem ipsum dolor sit amet, consectetuer adipiscing elit. Nam cursus. Morbi ut mi. Nullam enim leo, egestas id, condimentum at, laoreet mattis, massa.</p>
  <p class="body">Duis tincidunt lectus quis dui viverra vestibulum. Suspendisse vulputate aliquam dui. Nulla elementum dui ut augue. Aliquam vehicula mi at mauris. Maecenas placerat, nisl at consequat rhoncus, sem nunc gravida justo, quis eleifend arcu velit quis lacus. Morbi magna magna, tincidunt a, mattis non, imperdiet vitae, tellus. Sed odio est, auctor ac, sollicitudin in, consequat vitae, orci. Fusce id felis.</p>
</section>
<div class="abs badges">
  <div class="badge" style="width:60px"></div><div class="sep"></div>
  <div class="badge" style="width:55px"></div><div class="sep"></div>
  <div class="badge" style="width:68px"></div><div class="sep" style="margin:0 18px"></div>
  <div class="badge" style="width:30px;border-radius:50%"></div>
</div>

<section class="abs access">
  <h2>Private Access</h2>
  <p>Mauris vel lacus vitae felis vestibulum volutpat. Etiam est nunc, venenatis in, tristique eu</p>
  <div class="field">Acc. number</div>
  <div class="field">Acc. password</div>
  <div class="forgot"><span>forgot acc number/password?</span><span class="login">Login</span></div>
</section>

<footer class="abs footer">
  <div class="abs col" style="left:65px"><h4>About us</h4><ul><li>History</li><li>Expertise</li><li>Identity</li><li>Startegy</li><li>Contact Us</li></ul></div>
  <div class="abs col" style="left:170px"><h4>Investments</h4><ul><li>Term Deposits</li><li>Management &amp; Startegy</li><li>Client Relations</li><li>Financial Privacy</li><li>Tax Advice</li><li>Wealth Analy</li></ul></div>
  <div class="abs col" style="left:303px"><h4>Funds</h4><ul><li>Overview</li><li>Administration</li><li>Funds Security</li><li>Core Services</li><li>Reporting</li><li>Revenue Opprtunities</li><li>How ti Works</li></ul></div>
  <div class="abs col" style="left:442px"><h4>Currency Exchange</h4><ul><li>Foreign Exchange</li><li>Fx Forward</li><li>Fx Options</li></ul><h4 class="second">Accounts</h4><ul><li>Apply Now</li><li>Private Access</li></ul></div>
  <div class="abs col" style="left:589px"><h4>Brokerage</h4><ul><li style="line-height:17.6px">Institutional</li><li style="line-height:17.6px">Research</li><li style="line-height:17.6px">Trading</li></ul></div>
  <div class="abs rule"></div>
  <div class="abs copy">Copyright © 2013 Company Name.  All right reserved</div>
  <div class="abs social"><i style="background:#3b5a9a"></i><i style="background:#2ea6dc"></i><i style="background:#1c78b3"></i><i style="background:#ef7a1e"></i></div>
</footer>
</body>
</html>
```